The next stage in our 106 year history in Specialised Stationery

We need a business card design(which is also adaptable for our general stationery) to suit the changing face of our business. Harlow, an Australian company has been the leader in its category since 1907. We design and print various books required by small business to comply with government legislation in regards to keeping records. Accountancy, Payroll, Vehicle usage recording, Firearms registration etc. The Harlow logo a blue diamond is one of the best known in our industry. As manual recording has declined in the last few years we have diversified into other areas: Safety Apparel, Personal Protective Equipment (PPE) and web based software for bookkeeping and Customer Relationship management(CRM). Separate logos have been adopted for each of these being: Harlow Systems, Harlow Safety, Harlow Apparel and Harlow Software each with same diamond but different colour background. This has made it easy to identify the different sectors but difficult to bring together for a Corporate identity in Business cards etc. We are looking to bring all logos together (not one logo) but still allow the logo to depict the diversity of our offering, while still being able to have a category specific logo for each of the divisions. All products go through the same distribution channel, Office Products. The final design should depict an old established company well, known and trusted but leaping forward and still retaining same values they have come to trust.

Target Market(s)

Micro to small business companies generally who employ 20 or less people.

Industry/Entity Type

Small Business

Requirements
Must have
• The diamonds are well recognised and the new design should retain the integrity of them.

```html
<!DOCTYPE html>
<html lang="en">
<head>
<meta charset="utf-8">
<title>Harlow Business Card</title>
<link rel="stylesheet" href="https://fonts.googleapis.com/css2?family=Questrial&family=Roboto+Condensed:wght@400;700&display=swap">
<style>
  :root {
    --sky: #29abe2;
    --ocean: #1c75bc;
    --navy: #2e3192;
    --white: #ffffff;
    --ink: #111111;
    --page: #e8ebef;
  }
  * { box-sizing: border-box; margin: 0; padding: 0; }
  html, body {
    width: 1200px;
    height: 1200px;
    overflow: hidden;
    background: var(--page);
  }
  .sheet {
    width: 1200px;
    height: 1200px;
    display: flex;
    flex-direction: column;
    align-items: center;
    justify-content: center;
    gap: 60px;
  }
  .card {
    position: relative;
    width: 900px;
    height: 514px;
    border-radius: 28px;
    overflow: hidden;
    box-shadow: 0 6px 18px rgba(0, 0, 0, 0.15);
  }
  .card-art {
    position: absolute;
    inset: 0;
    width: 100%;
    height: 100%;
  }
  .front-backdrop {
    position: absolute;
    inset: 0;
    background: linear-gradient(160deg, var(--sky) 0%, var(--sky) 45%, var(--ocean) 100%);
  }
  .brand {
    position: absolute;
    display: flex;
    align-items: center;
    gap: 18px;
    font-family: "Roboto Condensed", sans-serif;
    font-weight: 700;
    color: var(--white);
    letter-spacing: 2px;
  }
  .brand-square {
    background: var(--navy);
  }
  .card-front .brand {
    left: 50%;
    top: 50%;
    transform: translate(-50%, -50%);
    font-size: 96px;
  }
  .card-front .brand-square { width: 70px; height: 70px; }
  .card-back .brand {
    left: 50%;
    top: 38px;
    transform: translateX(-50%);
    font-size: 60px;
  }
  .card-back .brand-square { width: 44px; height: 44px; }
  .contact {
    position: absolute;
    left: 70px;
    top: 265px;
    font-family: "Roboto Condensed", sans-serif;
    color: var(--ink);
  }
  .contact-web {
    font-size: 30px;
    margin-bottom: 10px;
  }
  .contact-line {
    display: flex;
    align-items: center;
    gap: 12px;
    font-size: 40px;
    line-height: 1.2;
  }
  .contact-icon {
    width: 46px;
    height: 46px;
    flex: none;
  }
  .company {
    position: absolute;
    right: 60px;
    top: 205px;
    text-align: center;
    color: var(--ink);
  }
  .company-name {
    font-family: "Questrial", sans-serif;
    font-size: 38px;
    margin-bottom: 10px;
    letter-spacing: 1px;
  }
  .company-address {
    font-family: "Roboto Condensed", sans-serif;
    font-size: 34px;
    line-height: 1.25;
  }
</style>
</head>
<body>
<main class="sheet">

  <section class="card card-front" aria-label="Card front">
    <div class="front-backdrop" role="img" aria-label="Abstract blue wave decoration"></div>
    <div class="brand">
      <span class="brand-square"></span>
      <span class="brand-name">HARLOW</span>
    </div>
  </section>

  <section class="card card-back" aria-label="Card back">
    <svg class="card-art" viewBox="0 0 900 514" preserveAspectRatio="none" aria-hidden="true">
      <rect width="900" height="514" fill="var(--white)"/>
      <path d="M0 0 H900 V140 L0 245 Z" fill="var(--ocean)"/>
      <rect x="0" y="432" width="900" height="82" fill="var(--navy)"/>
    </svg>

    <div class="brand">
      <span class="brand-square"></span>
      <span class="brand-name">HARLOW</span>
    </div>

    <div class="contact">
      <p class="contact-web">Web: www.harlow.com.au</p>
      <p class="contact-line">
        <svg class="contact-icon" viewBox="0 0 48 48" aria-label="Phone" role="img">
          <path d="M4 26 C4 14 44 14 44 26 L44 31 L33 31 L33 25 C28 22 20 22 15 25 L15 31 L4 31 Z" fill="var(--ink)"/>
        </svg>
        <span>61295550142</span>
      </p>
      <p class="contact-line">
        <svg class="contact-icon" viewBox="0 0 48 48" aria-label="Fax" role="img">
          <rect x="4" y="4" width="40" height="40" rx="3" fill="none" stroke="var(--ink)" stroke-width="3"/>
          <path d="M14 9 H28 L34 15 V33 H14 Z" fill="none" stroke="var(--ink)" stroke-width="2.5"/>
          <path d="M18 18 H30 M18 23 H30 M18 28 H30" stroke="var(--ink)" stroke-width="2"/>
          <rect x="10" y="35" width="28" height="6" fill="var(--ink)"/>
        </svg>
        <span>61295550187</span>
      </p>
    </div>

    <div class="company">
      <p class="company-name">Harlow Pty Limited</p>
      <p class="company-address">Unit 4, 212 Kingsway Road<br>Harbourfield, NSW 2299</p>
    </div>
  </section>

</main>
</body>
</html>
```